Real estate business card

I need a business card for my real estate company. I help clients buy and sell properties. I would like to keep the design very simple and professional. I would like the design to convey professionalism, safety and trust. I prefer no graphics but a simple logo design would be nice if that is part of what you do.
Updates

Please keep the designs simple. No high-rise buildings please. 

Reason: My design has not been finalized.

Target Market(s)

Age group 30-60 mostly affluent

Industry/Entity Type

Real Estate

Contact Information for Business Card

Velmont Realtors
Howard Prisk, Broker
4153 Marlow Ave. #226, La Crescenta, CA 91207

Requirements
Nice to have
• Logo can be combination of my initials HP or just Z or a simple geometric shape? Please see "Desig Ideas" attachment. No pics of houses or shaking hands, dollar bills, $, %, etc...
Please use fonts similar to Helvetica for a clean, modern look (think Northern European design, simple, clean yet bold)

Also use font colors such as blue, grey in different shades. Use pastel colors if better.

```html
<!DOCTYPE html>
<html lang="en">
<head>
<meta charset="utf-8">
<title>Velmont Realtors – Business Card</title>
<link rel="stylesheet" href="https://fonts.googleapis.com/css2?family=Montserrat:wght@300;400;700&display=swap">
<style>
  :root {
    --stage: #2b2b2d;
    --paper: #ffffff;
    --blue-deep: #1670b6;
    --blue-mid: #1592c6;
    --blue-light: #17a8cf;
    --ink-blue: #1a77b5;
    --ink-grey: #6d6e71;
    --ink-grey-light: #8a8b8e;
  }
  * { box-sizing: border-box; margin: 0; padding: 0; }
  html, body {
    width: 1200px; height: 1000px; overflow: hidden;
    background: var(--stage);
    font-family: "Montserrat", "Helvetica Neue", Arial, sans-serif;
  }
  .sheet {
    width: 1200px; height: 1000px;
    display: flex; flex-direction: column; align-items: center; justify-content: center;
    gap: 44px;
  }
  .card {
    position: relative;
    width: 720px; height: 411px;
    overflow: hidden;
    box-shadow: 0 10px 30px rgba(0,0,0,.45);
  }

  /* Back side */
  .card--back {
    background: linear-gradient(135deg, var(--blue-deep) 0%, var(--blue-light) 50%, var(--blue-deep) 100%);
  }
  .card--back .brand {
    position: absolute; left: 50%; top: 50%;
    transform: translate(-50%, -50%);
    color: var(--paper);
  }

  /* Brand lockup */
  .brand {
    display: flex; align-items: center; gap: 16px;
    font-weight: 700; letter-spacing: .02em;
    text-transform: uppercase; white-space: nowrap;
  }
  .brand__square {
    width: 58px; height: 58px; background: currentColor;
  }
  .brand__name { font-size: 30px; }

  /* Front side */
  .card--front { background: var(--paper); }
  .card--front .brand {
    position: absolute; left: 62px; top: 70px;
    color: var(--ink-blue);
  }
  .card--front .brand__name { font-size: 26px; }
  .card--front .brand__square { width: 52px; height: 52px; }

  .person {
    position: absolute; right: 62px; top: 56px; text-align: right;
  }
  .person__name { color: var(--ink-blue); font-weight: 700; font-size: 22px; letter-spacing: .02em; }
  .person__title { color: var(--ink-grey); font-weight: 300; font-size: 20px; margin-top: 2px; letter-spacing: .04em; }

  .contact {
    position: absolute; right: 62px; top: 196px;
    list-style: none; text-align: right;
    color: var(--ink-grey); font-weight: 300; font-size: 15px; letter-spacing: .04em;
  }
  .contact li { display: flex; justify-content: flex-end; align-items: center; gap: 10px; height: 24px; }
  .contact svg { width: 16px; height: 14px; fill: none; stroke: var(--ink-blue); stroke-width: 1.4; }
  .contact .contact__email { padding-right: 26px; }

  .address { position: absolute; left: 62px; top: 262px; }
  .address__label { color: var(--ink-blue); font-weight: 700; font-size: 18px; letter-spacing: .02em; }
  .address__lines { color: var(--ink-grey-light); font-weight: 300; font-size: 17px; line-height: 1.45; margin-top: 6px; letter-spacing: .03em; }

  .band {
    position: absolute; left: 0; right: 0; bottom: 0; height: 58px;
    background: linear-gradient(90deg, var(--blue-deep) 0%, var(--blue-light) 50%, var(--blue-deep) 100%);
  }
</style>
</head>
<body>
<main class="sheet">

  <section class="card card--back" aria-label="Card back">
    <div class="brand">
      <span class="brand__square"></span>
      <span class="brand__name">Velmont Realtors</span>
    </div>
  </section>

  <section class="card card--front" aria-label="Card front">
    <div class="brand">
      <span class="brand__square"></span>
      <span class="brand__name">Velmont Realtors</span>
    </div>

    <div class="person">
      <p class="person__name">Howard Prisk</p>
      <p class="person__title">Broker</p>
    </div>

    <ul class="contact">
      <li>818 555 0147
        <svg viewBox="0 0 16 14" aria-hidden="true"><rect x="5" y="0.8" width="6" height="12.4" rx="1"/><line x1="7.5" y1="11" x2="8.5" y2="11"/></svg>
      </li>
      <li>818 555 0192
        <svg viewBox="0 0 16 14" aria-hidden="true"><rect x="4" y="0.8" width="8" height="4"/><rect x="1" y="4.8" width="14" height="6"/><rect x="4" y="9" width="8" height="4.2"/></svg>
      </li>
      <li>hello@velmontrealtors.com
        <svg viewBox="0 0 16 14" aria-hidden="true"><rect x="1" y="2" width="14" height="10"/><polyline points="1,2 8,8 15,2"/></svg>
      </li>
    </ul>

    <div class="address">
      <p class="address__label">Address</p>
      <p class="address__lines">4153 Marlow Ave.<br>#226, La Crescenta, CA 91207</p>
    </div>

    <div class="band"></div>
  </section>

</main>
</body>
</html>
```